Marketing Skill "Workouts"; Design for an e-mail attachment highlighting Marketing training subjects

I am a freelance marketing trainer based in Singapore and need to e-mail out an attachment (probably saved as a PDF) to potential clients showing the training services I offer. These clients are all large blue-chip multinational companies so the attachment needs to look professional/high quality when opened on a computer.

My Company is called "Brightpath Marketing" (logo attached)

I am assuming the size should be A4 one sided colour.

I have attached some files that show best-attempts so far. These contain the key information, but the layouts all still look rather pedestrian. I am looking for something that looks a bit more dynamic but remains clear/easy to read.

Target Market(s)

HR/Marketing managers in multinational firms, mainly consumer goods

Industry/Entity Type

Marketing

Font styles to use
Sans Serif

Colors

Designer to choose colors to be used in the design.

Requirements
Must have
• Must look modern, up-to-date, professional.
Should not have
• Not gimmicky, like a cheap deal

```html
<!DOCTYPE html>
<html lang="en">
<head>
<meta charset="utf-8">
<title>Marketing Skill Workouts – Brightpath Marketing</title>
<link rel="stylesheet" href="https://fonts.googleapis.com/css2?family=Montserrat:ital,wght@0,800;1,500&family=Figtree:wght@400;500;600&display=swap">
<style>
  :root {
    --page-bg: #333333;
    --sheet-bg: #0c0c0c;
    --brand-red: #8e1a1b;
    --deep-red: #6a1f1c;
    --white: #ffffff;
    --ink: #111111;
    --panel-grey: rgba(196, 196, 196, 0.88);
    --text-light: #ececec;
  }
  * { box-sizing: border-box; margin: 0; padding: 0; }
  html, body {
    width: 1200px; height: 1200px; overflow: hidden;
    background: var(--page-bg);
    font-family: "Figtree", Arial, sans-serif;
  }
  .flyer {
    position: absolute; left: 36px; top: 184px;
    width: 1135px; height: 802px;
    background: var(--sheet-bg);
    overflow: hidden;
  }
  .hero-photo {
    position: absolute; left: 0; top: 0; width: 650px; height: 560px;
    background:
      radial-gradient(ellipse at 55% 45%, #5a3a28 0%, #3a2419 35%, #1a120d 65%, transparent 85%),
      linear-gradient(90deg, #2a2a2a 0%, #1a1a1a 20%, transparent 100%);
  }
  .contact-block {
    position: absolute; left: 778px; top: 0; width: 323px; height: 258px;
    background: var(--deep-red);
  }
  .logo-band {
    position: absolute; left: 0; top: 46px; width: 100%; height: 129px; z-index: 2;
    background: linear-gradient(90deg, transparent 0%, transparent 38%, rgba(150,150,150,0.55) 46%, #ffffff 82%);
  }
  .brand {
    position: absolute; right: 52px; top: 64px; height: 92px; z-index: 3;
    display: flex; align-items: center; gap: 14px;
  }
  .brand-name {
    font-family: "Figtree", Arial, sans-serif; font-weight: 500;
    font-size: 31px; line-height: 1; color: var(--ink);
  }
  .brand-mark {
    width: 88px; height: 88px; border-radius: 50%;
    background: var(--brand-red);
  }
  .contact {
    position: absolute; right: 62px; top: 186px; z-index: 3;
    text-align: right; color: var(--white);
    font-size: 19px; font-weight: 500; line-height: 28px;
  }
  .headline {
    position: absolute; left: 110px; top: 186px;
    font-family: "Montserrat", Arial, sans-serif; font-weight: 800;
    font-size: 53px; line-height: 60px; color: var(--white);
  }
  .headline .accent { display: block; color: var(--brand-red); }
  .lead {
    position: absolute; left: 110px; top: 320px; width: 432px;
    color: var(--white); font-weight: 500;
  }
  .lead-question { font-size: 22px; line-height: 28px; }
  .lead-body { font-size: 23px; line-height: 33px; margin-top: 16px; }
  .why-panel {
    position: absolute; left: 90px; top: 553px; width: 486px; height: 249px;
    background: var(--panel-grey);
    padding: 17px 36px 0 20px;
    color: var(--brand-red);
  }
  .why-title {
    font-family: "Montserrat", Arial, sans-serif; font-weight: 800; font-size: 16px;
  }
  .why-body { font-size: 14.5px; line-height: 19.5px; }
  .tagline-band {
    position: absolute; left: 0; top: 681px; width: 1115px; height: 73px;
    background: linear-gradient(90deg, var(--brand-red) 0%, #7e1b1b 55%, rgba(90,20,20,0.4) 85%, transparent 100%);
    display: flex; align-items: center; justify-content: center;
  }
  .tagline-band p {
    font-family: "Montserrat", Arial, sans-serif; font-style: italic; font-weight: 500;
    font-size: 41px; color: var(--white); letter-spacing: 0.3px;
  }
  .info-section { position: absolute; left: 633px; width: 470px; }
  .info-topics { top: 310px; }
  .info-benefits { top: 530px; }
  .info-title {
    font-family: "Montserrat", Arial, sans-serif; font-weight: 800;
    font-size: 28px; line-height: 34px; color: var(--brand-red);
  }
  .info-list { list-style: none; }
  .info-list li {
    position: relative;
    padding-left: 10px; color: var(--text-light);
    font-size: 15px; line-height: 19.5px;
  }
  .info-list li::before {
    content: ""; position: absolute; left: 0; top: 9px;
    width: 3px; height: 3px; background: var(--brand-red);
  }
</style>
</head>
<body>
<main class="flyer">
  <div class="hero-photo" role="img" aria-label="Dramatic dark photo of a muscular athlete lifting a dumbbell"></div>
  <div class="contact-block"></div>
  <div class="logo-band"></div>

  <div class="brand">
    <div class="brand-name">Brightpath Marketing</div>
    <div class="brand-mark"></div>
  </div>

  <div class="contact">
    <div>alexreyes@brightpath-marketing.com</div>
    <div>+65 9000 4127</div>
  </div>

  <h1 class="headline">Marketing skill<span class="accent">“Workouts”</span></h1>

  <div class="lead">
    <p class="lead-question">No time to learn?</p>
    <p class="lead-body">Problem solved with 1 day intensive workshops that will drive business growth and motivate your team</p>
  </div>

  <section class="info-section info-topics">
    <h2 class="info-title">Key Topics</h2>
    <ul class="info-list">
      <li>Developing strong brand plans</li>
      <li>Writing inspiring briefs/creative evaluation</li>
      <li>Shopper marketing/developing retail promotions</li>
      <li>Brilliant launch management</li>
      <li>Improving marketing R.O.I.</li>
      <li>Driving brand growth without product innovation</li>
      <li>Insight/concept development</li>
      <li>Integrating digital channels</li>
      <li>Creativity and idea generation</li>
    </ul>
  </section>

  <section class="info-section info-benefits">
    <h2 class="info-title">Key Benefits</h2>
    <ul class="info-list">
      <li>Latest in world-class thinking/tools/case studies</li>
      <li>Ability to ‘customise’ to address your specific business issue</li>
      <li>Take-away ‘checklists’ to embed behaviours and skills</li>
      <li>Asian context/relevance</li>
      <li>Proven quality</li>
    </ul>
  </section>

  <aside class="why-panel">
    <h3 class="why-title">Why me?</h3>
    <p class="why-body">The latest thinking, made practical and actionable.<br>20 years of business experience combined with over 10 years of proven training/facilitation for major “blue-chip” clients, regularly scoring 90%+ satisfaction</p>
  </aside>

  <div class="tagline-band">
    <p>World Class Quality without the costs</p>
  </div>
</main>
</body>
</html>
```